Büroausstattung Steuerberater
Alles prima. Frau Wendtke arbeitet äußerst professionell und wird von uns auch zukünftig für anstehende Arbeiten beauftragt!
Zielgruppe
Typisch Steuerberater: Vom jungen Existenzgründer bis zum Geschäftsführer eines großen Unternehmens.
Mit anderen Worten: Nicht verspielt, aber auch nicht zu bieder.
Aufgabenstellung
Wir benötigen:
-Allg. Briefpapier
-Rechnungsvorlage (mit einfacher Excel-Addition)
-Faxvorlage
-Visitenkarten
-Memo Block (DIN A4 - kariert)
Wichtig:
Wir benötigen nicht nur einen Designvorschlag, sondern fertige Word bzw. Excel Dokumente, mit denen wir direkt arbeiten bzw. diese ausdrucken können!
Da wir bereits ein Logo haben, ist die Kreierung eines Logos nicht erforderlich.

```html
<!DOCTYPE html>
<html lang="de">
<head>
<meta charset="utf-8">
<title>Geschäftsausstattung Steuerberater</title>
<link rel="stylesheet" href="https://fonts.googleapis.com/css2?family=Open+Sans:wght@400;600;700&family=Homemade+Apple&display=swap">
<style>
  :root {
    --brand-blue: #0d5a9c;
    --text-blue: #2b6cae;
    --ink: #1d1d1d;
    --paper: #ffffff;
    --board-light: #f2f2f2;
    --board-dark: #c9c9c9;
    --caption: #7a7a7a;
  }
  * { box-sizing: border-box; margin: 0; padding: 0; }
  html, body { width: 1200px; height: 1200px; overflow: hidden; }
  body {
    font-family: "Open Sans", Arial, sans-serif;
    color: var(--ink);
    background: var(--board-dark);
  }
  .board {
    position: absolute; left: 15px; top: 15px; width: 1170px; height: 1170px;
    background: radial-gradient(ellipse at 50% 40%, var(--board-light) 0%, #e3e3e3 55%, #d2d2d2 100%);
  }
  .sheet {
    position: absolute; background: var(--paper);
    box-shadow: 0 2px 8px rgba(0,0,0,.28);
  }
  .band { position: absolute; background: var(--brand-blue); }

  /* Letter */
  .letter { left: 75px; top: 75px; width: 684px; height: 966px; }
  .letter .band-top { left: 410px; top: 0; width: 208px; height: 15px; }
  .letter .band-bottom { left: 410px; top: 950px; width: 208px; height: 16px; }
  .fold-mark { position: absolute; left: 0; width: 16px; height: 2px; background: var(--brand-blue); }
  .wordmark {
    position: absolute; display: flex; align-items: center; gap: 8px;
    color: var(--text-blue); font-weight: 400; text-transform: uppercase; letter-spacing: .04em;
    white-space: nowrap;
  }
  .wordmark .mark { display: block; background: var(--text-blue); }
  .letter .wordmark { left: 410px; top: 90px; font-size: 18px; }
  .letter .wordmark .mark { width: 11px; height: 11px; }
  .sender-line {
    position: absolute; left: 78px; top: 165px; font-size: 7.5px; color: var(--text-blue);
    text-transform: uppercase; letter-spacing: .03em; white-space: nowrap;
  }
  .contact { position: absolute; font-size: 10.5px; line-height: 15px; color: var(--text-blue); }
  .letter .contact { left: 410px; top: 178px; }
  .contact dl { margin-top: 15px; display: grid; grid-template-columns: 42px auto; }
  .contact dt { font-weight: 700; }
  .recipient { position: absolute; left: 80px; top: 220px; font-size: 10.5px; line-height: 15px; font-style: normal; }
  .date { position: absolute; left: 410px; top: 306px; font-size: 10.5px; }
  .letter-body { position: absolute; left: 80px; top: 340px; width: 528px; font-size: 9.6px; line-height: 15px; }
  .subject { font-weight: 700; margin-bottom: 20px; }
  .letter-body p { margin-bottom: 14px; }
  .closing { position: absolute; left: 80px; top: 758px; font-size: 10px; line-height: 15px; }
  .signature { font-family: "Homemade Apple", cursive; font-size: 15px; line-height: 24px; margin: 2px 0 2px; }
  .footer-line {
    position: absolute; left: 78px; top: 948px; font-size: 7.5px; color: var(--text-blue);
    text-transform: uppercase; letter-spacing: .03em; white-space: nowrap;
  }

  /* Cards */
  .card { left: 713px; width: 444px; height: 255px; }
  .card-front { top: 300px; }
  .card-front .wordmark { left: 27px; top: 112px; font-size: 26px; }
  .card-front .wordmark .mark { width: 15px; height: 15px; }
  .card-back { top: 585px; height: 258px; }
  .card-back .band-top { left: 268px; top: 0; width: 176px; height: 22px; }
  .card-back .band-bottom { left: 226px; top: 232px; width: 147px; height: 26px; }
  .card-title { position: absolute; right: 72px; top: 45px; text-align: right; color: var(--text-blue); }
  .card-title .degree { font-size: 17px; line-height: 24px; }
  .card-title .name { font-size: 18px; font-weight: 700; line-height: 24px; }
  .card-title .role { font-size: 11.5px; line-height: 16px; }
  .card-back .contact { left: 27px; top: 136px; font-size: 11.5px; line-height: 15px; }
  .card-back .contact dl { grid-template-columns: 60px auto; margin-top: 12px; }

  .caption {
    position: absolute; left: 78px; top: 1065px; font-size: 23px; font-weight: 700; color: var(--caption);
  }
</style>
</head>
<body>
<main class="board">

  <article class="sheet letter">
    <div class="band band-top"></div>
    <div class="wordmark"><span class="mark"></span>Jens Hallwachs</div>
    <span class="fold-mark" style="top:342px"></span>
    <span class="fold-mark" style="top:481px"></span>
    <span class="fold-mark" style="top:684px"></span>

    <div class="sender-line">Jens Hallwachs &nbsp;|&nbsp; Musterstr. 123 &nbsp;|&nbsp; 01234 Musterstadt</div>

    <div class="contact">
      Musterstr. 123<br>01234 Musterstadt
      <dl>
        <dt>PHONE:</dt><dd>+41 41 5550188</dd>
        <dt>MAIL:</dt><dd>max@beispielkanzlei.de</dd>
        <dt>WEB:</dt><dd>www.beispielkanzlei.de</dd>
      </dl>
    </div>

    <address class="recipient">Frau<br>Maria Mustermann<br>Feldstraße 1<br>11111 Musterstadt</address>
    <div class="date">Musterstadt, 17. Februar 2011</div>

    <div class="letter-body">
      <p class="subject">Betreffzeile</p>
      <p>Sehr geehrte Frau Mustermann,</p>
      <p>dies ist ein Typoblindtext. An ihm kann man sehen, ob alle Buchstaben da sind und wie sie aussehen. Manchmal benutzt man Worte wie Hamburgefonts, Rafgenduks oder Handgloves, um Schriften zu testen. Manchmal Sätze, die alle Buchstaben des Alphabets enthalten - man nennt diese Sätze »Pangrams«. Sehr bekannt ist dieser: The quick brown fox jumps over the lazy old dog. Oft werden in Typoblindtexte auch fremdsprachige Satzteile eingebaut (AVAIL® and Wefox™ are testing aussi la Kerning), um die Wirkung in anderen Sprachen zu testen. In Lateinisch sieht zum Beispiel fast jede Schrift gut aus. Quod erat demonstrandum. Seit 1975 fehlen in den meisten Testtexten die Zahlen, weswegen nach TypoGb. 204 § ab dem Jahr 2034 Zahlen in 86 der Texte zur Pflicht werden. Nichteinhaltung wird mit bis zu 245 € oder 368 $ bestraft.</p>
      <p>Genauso wichtig in sind mittlerweile auch Âçcèñtë, die in neueren Schriften aber fast immer enthalten sind. Ein wichtiges aber schwierig zu integrierendes Feld sind OpenType-Funktionalitäten. Je nach Software und Voreinstellungen können eingebaute Kapitälchen, Kerning oder Ligaturen (sehr pfiffig) nicht richtig dargestellt werden. Dies ist ein Typoblindtext. An ihm kann man sehen, ob alle Buchstaben da sind und wie sie aussehen. Manchmal benutzt man Worte wie Hamburgefonts, Rafgenduks oder Handgloves, um Schriften zu testen. Manchmal Sätze, die alle Buchstaben des Alphabets enthalten - man nennt diese Sätze »Pangrams«.</p>
      <p>Seit 1975 fehlen in den meisten Testtexten die Zahlen, weswegen nach TypoGb. 204 § ab dem Jahr 2034 Zahlen in 86 der Texte zur Pflicht werden. Nichteinhaltung wird mit bis zu 245 € oder 368 $ bestraft. Genauso wichtig in sind mittlerweile auch Âçcèñtë, die in neueren Schriften aber fast immer enthalten sind. Ein wichtiges aber schwierig zu integrierendes Feld sind OpenType-Funktionalitäten. Je nach Software und Voreinstellungen können eingebaute Kapitälchen, Kerning oder Ligaturen (sehr pfiffig) nicht richtig dargestellt werden.</p>
    </div>

    <div class="closing">
      Mit freundlichen Grüßen<br><br>
      Firma Mustermann
      <div class="signature">Mustermann</div>
      Max Mustermann
    </div>

    <div class="footer-line">Bank Musterstadt &nbsp;|&nbsp; BLZ 123 456 78 &nbsp;|&nbsp; Konto 0 123 456 789</div>
    <div class="band band-bottom"></div>
  </article>

  <section class="sheet card card-front">
    <div class="wordmark"><span class="mark"></span>Jens Hallwachs</div>
  </section>

  <section class="sheet card card-back">
    <div class="band band-top"></div>
    <div class="card-title">
      <div class="degree">Dipl. Kaufmann</div>
      <div class="name">Jens Hallwachs</div>
      <div class="role">Steuerberater</div>
    </div>
    <div class="contact">
      Musterstr. 123<br>01234 Musterstadt
      <dl>
        <dt>PHONE:</dt><dd>+41 41 5550188</dd>
        <dt>MAIL:</dt><dd>max@beispielkanzlei.de</dd>
        <dt>WEB:</dt><dd>www.beispielkanzlei.de</dd>
      </dl>
    </div>
    <div class="band band-bottom"></div>
  </section>

  <p class="caption">Geschäftsbrief nach DIN 676b</p>
</main>
</body>
</html>
```